Northgate Roofing Works Inc Business cards

Commercial and Residential Roofing contractor needs design logo and card design. Can be single or double sided but must incorporate:
Persons Name:
Persons Title:
Mailing Address: PO Box 3719
Physical Address: 58 Fenwick Lane
Harlow, Ma. 01642
800-316-5842
508-712-5842
Fax: 508-712-5867
Cell: Person Cell number
email address
Website: WWW.northgateroofworks.com

Target Market(s)

Residential home owners and commercial building owners

Industry/Entity Type

Roofing

Contact Information for Business Card

Persons Name:
Persons Title:
Harlow, Ma. 01642
800-316-5842
508-712-5842
Fax: 508-712-5867
Cell: Person Cell number
email address

Logo Text

Large enough to service small enough to care

Font styles to use
Serif

Colors
0355a3

Requirements
Must have
• Commercial and Residential Roofing contractor needs design logo and card design. Can be single or double sided but must incorporate:
• Persons Name:
• Persons Title:
• Mailing Address: PO Box 3719
• Physical Address: 58 Fenwick Lane
• Harlow, Ma. 01642
• 800-316-5842
• 508-712-5842
• Fax: 508-712-5867
• Cell: Person Cell number
• email address
• Website: WWW.northgateroofworks.com
Nice to have
• ..
Should not have
• I'm looking for something different. I have had the same card for 23 years. I attached what both sides of my present card looks like.

```html
<!DOCTYPE html>
<html lang="en">
<head>
<meta charset="utf-8">
<title>Northgate Roofing Works – Business Card</title>
<link rel="stylesheet" href="https://fonts.googleapis.com/css2?family=Open+Sans:wght@400;600&display=swap">
<style>
  :root {
    --brand-blue: #0b57a6;
    --ink: #4a4a4a;
    --paper: #ffffff;
    --backdrop: #5a5a5a;
  }
  html, body {
    margin: 0;
    padding: 0;
    width: 1200px;
    height: 1200px;
    overflow: hidden;
    background: var(--backdrop);
    font-family: "Open Sans", Arial, sans-serif;
  }
  .card {
    position: absolute;
    left: 253px;
    width: 696px;
    height: 395px;
    box-shadow: 0 4px 10px rgba(0,0,0,0.45);
    box-sizing: border-box;
  }
  .card--front { top: 165px; background: var(--paper); }
  .card--back  { top: 642px; background: var(--brand-blue); }

  .name-bar {
    position: absolute;
    left: 0; top: 86px;
    width: 14px; height: 42px;
    background: var(--brand-blue);
  }
  .person {
    position: absolute;
    left: 30px; top: 80px;
  }
  .person__name {
    margin: 0;
    font-size: 26px;
    font-weight: 400;
    color: var(--brand-blue);
    line-height: 1.2;
  }
  .person__title {
    margin: 0;
    font-size: 17px;
    color: var(--ink);
    line-height: 1.3;
  }
  .address {
    position: absolute;
    left: 30px; top: 155px;
    margin: 0;
    font-size: 17px;
    line-height: 23px;
    color: var(--ink);
    font-style: normal;
  }
  .contacts {
    position: absolute;
    left: 30px; top: 220px;
    margin: 0; padding: 0;
    list-style: none;
  }
  .contacts li {
    display: flex;
    align-items: center;
    height: 23.3px;
    font-size: 17px;
    color: var(--ink);
  }
  .contacts svg {
    width: 20px; height: 18px;
    margin-right: 12px;
    fill: var(--brand-blue);
    flex: none;
  }
  .wordmark {
    position: absolute;
    display: flex;
    align-items: center;
    gap: 10px;
    font-weight: 600;
    white-space: nowrap;
  }
  .wordmark__square { flex: none; }
  .card--front .wordmark {
    left: 372px; top: 152px;
    font-size: 22px;
    color: var(--brand-blue);
  }
  .card--front .wordmark__square { width: 20px; height: 20px; background: var(--brand-blue); }
  .card--back .wordmark {
    left: 50%; top: 228px;
    transform: translateX(-50%);
    font-size: 22px;
    color: var(--paper);
  }
  .card--back .wordmark__square { width: 18px; height: 18px; background: var(--paper); }
</style>
</head>
<body>
  <section class="card card--front">
    <div class="name-bar"></div>
    <div class="person">
      <h1 class="person__name">Daniel Hartwell</h1>
      <p class="person__title">Managing Partner</p>
    </div>
    <address class="address">Physical Address: 58 Fenwick Lane<br>Harlow, Ma. 01642</address>
    <ul class="contacts">
      <li><svg viewBox="0 0 20 18"><path d="M1 6c0-3 4-5 9-5s9 2 9 5v2h-5V6H6v2H1z"/><path d="M4 9l2-2h8l2 2v8H4z"/><circle cx="10" cy="12.5" r="2.4" fill="#fff"/></svg>800-316-5842</li>
      <li><svg viewBox="0 0 20 18"><path d="M1 6c0-3 4-5 9-5s9 2 9 5v2h-5V6H6v2H1z"/><path d="M4 9l2-2h8l2 2v8H4z"/><circle cx="10" cy="12.5" r="2.4" fill="#fff"/></svg>508-712-5842</li>
      <li><svg viewBox="0 0 20 18"><rect x="5" y="0" width="10" height="5"/><rect x="1" y="6" width="18" height="7" rx="1.5"/><rect x="5" y="11" width="10" height="7"/><rect x="7" y="13" width="6" height="1.5" fill="#fff"/></svg>508-712-5867</li>
      <li><svg viewBox="0 0 20 18"><rect x="5" y="0" width="10" height="18" rx="2"/><rect x="6.5" y="2" width="7" height="12" fill="#fff"/><circle cx="10" cy="16" r="1" fill="#fff"/></svg>Person Cell number</li>
      <li><svg viewBox="0 0 20 18"><rect x="0" y="3" width="20" height="13"/><path d="M0.5 3.5L10 11l9.5-7.5M0.5 15.5l7-6M19.5 15.5l-7-6" stroke="#fff" stroke-width="1.3" fill="none"/></svg>email address</li>
      <li><svg viewBox="0 0 20 18"><g fill="none" stroke="#0b57a6" stroke-width="1.3"><circle cx="10" cy="9" r="8"/><ellipse cx="10" cy="9" rx="3.5" ry="8"/><path d="M2 9h16M3.5 4.5h13M3.5 13.5h13M10 1v16"/></g></svg>www.northgateroofworks.com</li>
    </ul>
    <div class="wordmark"><span class="wordmark__square"></span>Northgate Roofing Works</div>
  </section>

  <section class="card card--back">
    <div class="wordmark"><span class="wordmark__square"></span>Northgate Roofing Works</div>
  </section>
</body>
</html>
```